ebook cover: book 4 in the We Hum Lantern series. Lantern by Riverside

I am wanting a striking cover to bring the forth book in a spiritual journey series to an audience ready to meet new characters and get excited again! White backgrounds, red titles (any font), subtitles to introduce a new major character in the series of ten (same fonts please as the original, We Hum Lantern), and one emblematic, slightly mysterious image. Please keep to the same colour tones as the original, but the lead image need not be gray. Let's please try to use the "light flash" that is on the tin can in We Hum Lantern somehow, in your own way. It is meant to signify the other side, or the higher light, or some such inference.

Book details:
Title: Lantern by Riverside
Subtitle: Archangel Veloriel brings the message
Image: silver hourglass
Author: Maren Tulliver, Ph.D
Strap quote: "Tulliver is smart, savvy and full of ideas," Harbourgate Ledger

Please do your best: this one is going in competition of spiritual healers!

Thanks! :)

```html
<!DOCTYPE html>
<html lang="en">
<head>
<meta charset="utf-8">
<title>Lantern by Riverside — Maren Tulliver Ph.D.</title>
<link rel="stylesheet" href="https://fonts.googleapis.com/css2?family=Open+Sans:wght@400;600;700&family=Playfair+Display:wght@700;900&display=swap">
<style>
  :root {
    --backdrop: #111111;
    --cover-white: #f4f8fb;
    --title-red-light: #d3161d;
    --title-red-dark: #7f0a0e;
    --ink: #1b1b1b;
    --author-grey: #5a5a5a;
    --silver-light: #fbfcfd;
    --silver-mid: #d5d9dd;
    --silver-dark: #8d939a;
  }
  * { margin: 0; padding: 0; box-sizing: border-box; }
  html, body {
    width: 923px;
    height: 1200px;
    overflow: hidden;
    background: var(--backdrop);
  }
  .book-cover {
    position: absolute;
    left: 88px;
    top: 66px;
    width: 722px;
    height: 1069px;
    background: var(--cover-white);
    text-align: center;
  }
  .strap-quote {
    position: absolute;
    top: 6px;
    left: 0;
    width: 100%;
    font-family: "Open Sans", sans-serif;
    font-weight: 700;
    font-size: 13px;
    letter-spacing: 0.2px;
    color: var(--ink);
    text-transform: uppercase;
  }
  .strap-quote .source { font-size: 16px; font-weight: 600; }
  .title-line {
    position: absolute;
    left: 0;
    width: 100%;
    font-family: "Playfair Display", serif;
    font-weight: 700;
    font-size: 104px;
    line-height: 1;
    letter-spacing: -3px;
    text-transform: uppercase;
    background: linear-gradient(180deg, var(--title-red-light) 0%, var(--title-red-light) 45%, var(--title-red-dark) 100%);
    -webkit-background-clip: text;
    background-clip: text;
    color: transparent;
    transform: scaleX(0.82);
  }
  .title-line.first { top: 86px; }
  .title-line.second { top: 198px; }
  .subtitle {
    position: absolute;
    top: 338px;
    left: 0;
    width: 100%;
    font-family: "Open Sans", sans-serif;
    font-weight: 400;
    font-size: 27px;
    line-height: 42px;
    letter-spacing: 4.5px;
    color: var(--ink);
    text-transform: uppercase;
  }
  .lead-image {
    position: absolute;
    left: 229px;
    top: 458px;
    width: 280px;
    height: 476px;
    border-radius: 18px;
    background:
      radial-gradient(circle at 66% 16%, #ffffff 0 4%, rgba(255,255,255,0) 14%),
      linear-gradient(90deg, var(--silver-dark) 0%, var(--silver-mid) 18%, var(--silver-light) 50%, var(--silver-mid) 82%, var(--silver-dark) 100%);
  }
  .author {
    position: absolute;
    top: 996px;
    left: 0;
    width: 100%;
    font-family: "Open Sans", sans-serif;
    font-weight: 400;
    font-size: 33px;
    letter-spacing: 3px;
    color: var(--author-grey);
    text-transform: uppercase;
  }
  .author .credential-small { font-size: 24px; }
</style>
</head>
<body>
  <main class="book-cover">
    <p class="strap-quote">"Tulliver is smart, savvy and full of ideas" - <span class="source">Harbourgate Ledger</span></p>
    <h1 class="title">
      <span class="title-line first">Lantern by</span>
      <span class="title-line second">Riverside</span>
    </h1>
    <h2 class="subtitle">Archangel Veloriel<br>brings the message</h2>
    <div class="lead-image" role="img" aria-label="Silver hourglass with white sand and a bright flash of light on its frame"></div>
    <p class="author">Maren Tulliver P<span class="credential-small">h.D.</span></p>
  </main>
</body>
</html>
```